Redesign of an insurance website

Attached is an insurance website that I need to redesign. Currently the website is too dark. I like for example www.brenvalo.com . Could you make the website lighter and change the structure a little so that it is more user friendly?

Industry/Entity Type

Insurance

Number of Pages Required

4 page

```html
<!DOCTYPE html>
<html lang="cs">
<head>
<meta charset="utf-8">
<title>KRYTOVKA.CZ – Pojištění</title>
<link href="https://fonts.googleapis.com/css2?family=Poppins:wght@400;500;600;700&family=Roboto:wght@500;700&display=swap" rel="stylesheet">
<style>
:root{
  --blue:#2a7ff4;
  --orange:#f97b1c;
  --ink:#333333;
  --light:#f7f7f7;
  --line:#e6e6e6;
  --dark:#404040;
  --white:#ffffff;
  --icon:#555555;
}
*{box-sizing:border-box;margin:0;padding:0}
html,body{width:1200px;height:2359px;overflow:hidden}
body{position:relative;background:var(--white);font-family:'Poppins',sans-serif;color:var(--ink)}
.abs{position:absolute}
.defs{position:absolute;width:0;height:0}

/* header */
.site-header{position:absolute;left:0;top:0;width:1200px;height:69px;border-bottom:2px solid #ececec;background:var(--white)}
.brand{position:absolute;left:113px;top:14px;font-weight:700;font-size:28px;letter-spacing:.5px;color:var(--blue)}
.main-nav a{position:absolute;top:25px;font-family:'Roboto',sans-serif;font-weight:500;font-size:13px;color:#222;text-decoration:none}
.auth{position:absolute;left:925px;top:16px;width:163px;height:34px;border-radius:17px;background:var(--orange);display:flex;align-items:center;font-family:'Roboto',sans-serif;font-weight:700;font-size:10.5px;color:var(--white)}
.auth span{flex:1;text-align:center}
.auth span:first-child{flex:0 0 58px;border-right:1px solid rgba(255,255,255,.5)}

/* quote form */
.quote-card{position:absolute;left:112px;top:153px;width:333px;height:456px;background:#fafaf6;box-shadow:0 10px 14px rgba(0,0,0,.12)}
.quote-card h2{height:77px;background:var(--blue);color:var(--white);font-weight:600;font-size:20px;line-height:26px;text-align:center;padding-top:12px}
.quote-icon{position:absolute;left:114px;top:94px;width:104px;height:104px;border:3px solid var(--orange);border-radius:50%;background:var(--white);display:flex;align-items:center;justify-content:center;color:#222}
.field{position:absolute;left:17px;width:299px;height:33px;background:var(--white);border:1px solid #e8e8e8;font-size:12px;padding:8px 10px;color:#333}
.agree{position:absolute;left:17px;top:347px;font-size:11px;color:#888;display:flex;align-items:center;gap:8px}
.agree i{width:12px;height:12px;border:1px solid #ccc;background:var(--white)}
.quote-btn{position:absolute;left:17px;top:388px;width:145px;height:42px;background:var(--orange);color:var(--white);font-weight:600;font-size:12px;text-align:center;line-height:42px}

/* product grid */
.product{position:absolute;width:180px;text-align:center;font-size:14px;color:#555}
.product .ring{width:88px;height:88px;margin:0 auto 10px;border:2px solid var(--blue);border-radius:50%;display:flex;align-items:center;justify-content:center;background:var(--white);color:var(--icon)}
.product.active .ring{border-color:var(--orange);color:#222}
.product.active{color:#222;font-weight:500}
.agent-btn{position:absolute;left:458px;top:695px;width:284px;height:61px;border-radius:31px;background:var(--blue);color:var(--white);font-family:'Roboto',sans-serif;font-weight:500;font-size:15px;text-align:center;line-height:61px;box-shadow:0 10px 14px rgba(42,127,244,.3)}

/* how it works */
.how{position:absolute;left:0;top:829px;width:1200px;height:376px;background:var(--light);border-top:1px solid var(--line)}
.section-title{position:absolute;left:0;width:1200px;text-align:center;font-weight:600;font-size:25px;color:var(--ink)}
.step{position:absolute;width:240px;text-align:center;font-size:16px;line-height:25px;color:#222}
.step .disc{width:132px;height:132px;margin:0 auto 12px;border-radius:50%;background:var(--white);border:6px solid #eeeeee;box-shadow:0 0 0 1px #ddd;display:flex;align-items:center;justify-content:center}

/* promo band */
.promo{position:absolute;left:0;top:1205px;width:1200px;height:412px;background:linear-gradient(110deg,#f3a56a 0%,#f0915a 35%,#f58b34 70%,#f6852a 100%);color:var(--white);text-align:center}
.promo h2{position:absolute;left:0;width:1200px;top:98px;font-weight:600;font-size:35px}
.promo p{position:absolute;left:120px;width:960px;top:178px;font-size:13px;line-height:25px}
.promo .more{position:absolute;left:535px;top:314px;width:145px;height:43px;background:var(--white);color:var(--orange);font-weight:600;font-size:12px;line-height:43px}

/* reviews */
.review{position:absolute;top:1788px;width:300px}
.review .q{position:absolute;left:0;top:0;width:50px;height:50px;border-radius:50%;background:var(--blue);color:var(--white);font-size:34px;font-weight:700;line-height:62px;text-align:center}
.review h3{position:absolute;left:64px;top:2px;font-size:15px;font-weight:600;color:var(--blue);white-space:nowrap}
.review .sub{position:absolute;left:64px;top:26px;font-size:11.5px;color:#777;white-space:nowrap}
.review p{position:absolute;left:0;top:64px;width:300px;font-size:11px;line-height:19px;color:#666}
.review .name{position:absolute;left:0;top:212px;font-size:12.5px;font-weight:600;color:var(--blue)}
.review .rate{position:absolute;left:0;top:231px;display:flex;align-items:center;gap:2px;font-size:10px;color:#999}
.review .rate em{font-style:normal;margin-left:12px;text-decoration:underline}

/* newsletter */
.newsletter{position:absolute;left:0;top:2103px;width:1200px;height:108px;background:var(--orange);color:var(--white)}
.newsletter h2{position:absolute;left:111px;top:30px;font-weight:500;font-size:21px}
.newsletter small{position:absolute;left:111px;top:60px;font-size:12px}
.newsletter .mail{position:absolute;left:420px;top:33px;width:239px;height:39px;background:var(--white);font-size:12px;color:#999;padding:11px 10px}
.newsletter .sub-btn{position:absolute;left:675px;top:33px;width:107px;height:39px;background:var(--blue);font-weight:600;font-size:12px;text-align:center;line-height:39px}
.social{position:absolute;top:32px;width:44px;height:44px;border:2px solid var(--white);border-radius:50%;font-size:9px;font-weight:600;line-height:40px;text-align:center;color:var(--white)}

/* footer */
.site-footer{position:absolute;left:0;top:2211px;width:1200px;height:148px;background:var(--dark);color:var(--white)}
.contact{position:absolute;top:30px;display:flex;align-items:center;gap:18px}
.contact .dot{flex:0 0 30px;width:30px;height:30px;border-radius:50%;background:var(--orange);display:flex;align-items:center;justify-content:center}
.footer-rule{position:absolute;left:0;top:88px;width:1200px;height:1px;background:#555}
.footer-nav a{position:absolute;top:109px;font-size:12px;color:var(--white);text-decoration:none}
.copy{position:absolute;right:113px;top:110px;font-size:11px}
</style>
</head>
<body>

<svg class="defs" aria-hidden="true">
  <defs>
    <symbol id="crash" viewBox="0 0 60 44">
      <g fill="currentColor">
        <g transform="rotate(-14 17 28)">
          <path d="M6 20l4-9h14l4 9z"/>
          <rect x="2" y="20" width="30" height="12" rx="3"/>
          <rect x="5" y="31" width="6" height="5" rx="1"/>
          <rect x="23" y="31" width="6" height="5" rx="1"/>
          <path d="M10.5 19.5l2.5-6h8l2.5 6z" fill="#fff"/>
          <circle cx="7.5" cy="26" r="2.2" fill="#fff"/>
          <circle cx="26.5" cy="26" r="2.2" fill="#fff"/>
        </g>
        <g transform="rotate(14 43 28)">
          <path d="M32 20l4-9h14l4 9z"/>
          <rect x="28" y="20" width="30" height="12" rx="3"/>
          <rect x="31" y="31" width="6" height="5" rx="1"/>
          <rect x="49" y="31" width="6" height="5" rx="1"/>
          <path d="M36.5 19.5l2.5-6h8l2.5 6z" fill="#fff"/>
          <circle cx="33.5" cy="26" r="2.2" fill="#fff"/>
          <circle cx="52.5" cy="26" r="2.2" fill="#fff"/>
        </g>
      </g>
      <path d="M30 1v7M23 3l3 5M37 3l-3 5" stroke="currentColor" stroke-width="2" stroke-linecap="round"/>
    </symbol>
    <symbol id="globe" viewBox="0 0 50 50">
      <circle cx="27" cy="22" r="18" fill="currentColor"/>
      <path d="M6 38l16-4 18-12-2-2-18 8-8-4-3 2 6 6-9 4z" fill="#fff" stroke="currentColor" stroke-width="1.5"/>
    </symbol>
    <symbol id="car" viewBox="0 0 54 24">
      <path d="M2 18v-6l8-2 8-7h16l10 7 8 2v6z" fill="currentColor"/>
      <path d="M20 5h6v5h-11zM29 5h4l6 5h-10z" fill="#fff"/>
      <circle cx="14" cy="19" r="4" fill="#fff" stroke="currentColor" stroke-width="2"/>
      <circle cx="41" cy="19" r="4" fill="#fff" stroke="currentColor" stroke-width="2"/>
    </symbol>
  </defs>
</svg>

<header class="site-header">
  <div class="brand">KRYTOVKA.CZ</div>
  <nav class="main-nav">
    <a style="left:635px">ABOUT US</a>
    <a style="left:761px">FAQ</a>
    <a style="left:832px">CONTACT</a>
  </nav>
  <div class="auth"><span>LOGIN</span><span>REGISTER NOW</span></div>
</header>

<section class="quote-card">
  <h2>NAJDETE NEJVYHODNEJSI<br>POJISTENI</h2>
  <div class="quote-icon"><svg width="66" height="48"><use href="#crash"/></svg></div>
  <div class="field" style="top:217px">Name:</div>
  <div class="field" style="top:259px">Sur Name:</div>
  <div class="field" style="top:300px">Email:</div>
  <div class="agree"><i></i>Souhlasim S Podminkami Pouziti</div>
  <div class="quote-btn">SPOCITAT CENU</div>
</section>

<div class="product active" style="left:501px;top:168px"><div class="ring"><svg width="54" height="40"><use href="#crash"/></svg></div>Havarijni Pojisteni</div>
<div class="product" style="left:693px;top:168px"><div class="ring"><svg width="50" height="50"><use href="#globe"/></svg></div>Cestovni Pojisteni</div>
<div class="product" style="left:884px;top:168px"><div class="ring"><svg width="54" height="24"><use href="#car"/></svg></div>Povinne Ruceni</div>

<div class="product" style="left:501px;top:324px"><div class="ring"><svg width="46" height="42" viewBox="0 0 46 42"><path d="M23 2L2 21h6v19h11V28h8v12h11V21h6z" fill="currentColor"/></svg></div>Havarijni Pojisteni</div>
<div class="product" style="left:693px;top:324px"><div class="ring"><svg width="50" height="50"><use href="#globe"/></svg></div>Cestovni Pojisteni</div>
<div class="product" style="left:884px;top:324px"><div class="ring"><svg width="54" height="40"><use href="#crash"/></svg></div>Domova Pojisteni</div>

<div class="product" style="left:501px;top:480px"><div class="ring"><svg width="54" height="40"><use href="#crash"/></svg></div>Havarijni Pojisteni</div>
<div class="product" style="left:693px;top:480px"><div class="ring"><svg width="50" height="50"><use href="#globe"/></svg></div>Cestovni Pojisteni</div>
<div class="product" style="left:884px;top:480px"><div class="ring"><svg width="54" height="24"><use href="#car"/></svg></div>Domova Pojisteni</div>

<div class="agent-btn">FIND AN AGENT NEAR YOU</div>

<section class="how">
  <h2 class="section-title" style="top:46px">JAK TO FUNGUJE</h2>
  <div class="step" style="left:172px;top:124px"><div class="disc"><svg width="50" height="50" viewBox="0 0 50 50"><path d="M4 24a21 21 0 0 1 42 0z" fill="#2a7ff4"/><path d="M25 24v16a4 4 0 0 1-8 0" fill="none" stroke="#2a7ff4" stroke-width="3"/></svg></div>Choose Any Of Our<br>Insurance</div>
  <svg class="abs" style="left:385px;top:168px" width="115" height="40" viewBox="0 0 115 40"><path d="M2 30Q50 -6 105 24" fill="none" stroke="#ccc" stroke-width="1.5"/><path d="M100 18l8 8-10 1z" fill="#bbb"/></svg>
  <div class="step" style="left:479px;top:124px"><div class="disc"><svg width="50" height="50" viewBox="0 0 50 50"><rect x="8" y="8" width="28" height="36" rx="3" fill="none" stroke="#2a7ff4" stroke-width="3"/><rect x="16" y="4" width="12" height="8" rx="2" fill="#2a7ff4"/><path d="M14 20h16M14 27h16M14 34h8" stroke="#2a7ff4" stroke-width="3"/><circle cx="37" cy="37" r="9" fill="#2a7ff4"/><path d="M33 37l3 3 5-6" fill="none" stroke="#fff" stroke-width="2.5"/></svg></div>Claim Your<br>Insurance</div>
  <svg class="abs" style="left:690px;top:168px" width="115" height="40" viewBox="0 0 115 40"><path d="M2 10Q50 50 105 16" fill="none" stroke="#ccc" stroke-width="1.5"/><path d="M98 12l10 2-6 8z" fill="#bbb"/></svg>
  <div class="step" style="left:780px;top:124px"><div class="disc"><svg width="52" height="52" viewBox="0 0 52 52"><circle cx="24" cy="28" r="19" fill="none" stroke="#2a7ff4" stroke-width="4"/><path d="M14 27l9 9L46 6" fill="none" stroke="#2a7ff4" stroke-width="5" stroke-linecap="round"/></svg></div>Become our Satisfied<br>Customer</div>
</section>

<section class="promo" role="img" aria-label="Oranžový pás s jemným geometrickým vzorem na pozadí">
  <h2>Uzavreli Jste V Minulosti Nevyhodnou Pojistku?</h2>
  <p>Lorem ipsum dolor sit amet, consectetuer adipiscing elit, sed diam nonummy nibh euismod tincidunt ut laoreet dolore magna aliquam erat volutpat. Ut wisi enim ad minim veniam, quis nostrud exerci tation ullamcorper suscipit lobortis nisl ut aliquip ex ea commodo consequat. Duis autem vel eum iriure dolor in hendrerit in vulputate velit esse molestie consequat, vel illum dolore eu feugiat nulla facilisis at vero eros et accumsan et iusto odio dignissim qui blandit praesent luptatum zzril delenit augue duis dolore te feugait nulla facilisi.</p>
  <div class="more">READ MORE</div>
</section>

<h2 class="section-title" style="top:1698px">CUSTOMER REVIEW</h2>

<article class="review" style="left:112px">
  <div class="q">&ldquo;</div>
  <h3>Consectetuer Adipiscing Elit</h3>
  <div class="sub">Sed Diam Nonummy Nibh Euismod...</div>
  <p>Lorem ipsum dolor sit amet, consectetuer adipiscing elit, sed diam nonummy nibh euismod tincid laoreet dolore magna aliquam erat volutpat. Ut wisi enim ad minim veniam, quis nostrud extation ullamcorper suscipit lobortis nisl ut aliquip commodo consequat. Duis autem veum iriure dolor in hendrerit in vulputate velit esse molestie consequat.</p>
  <div class="name">Customer Name</div>
  <div class="rate"><span style="color:#f97b1c">★★★★</span><span style="color:#bbb">★</span><em>30 Review</em></div>
</article>
<article class="review" style="left:450px">
  <div class="q">&ldquo;</div>
  <h3>Consectetuer Adipiscing Elit</h3>
  <div class="sub">Sed Diam Nonummy Nibh Euismod...</div>
  <p>Lorem ipsum dolor sit amet, consectetuer adipiscing elit, sed diam nonummy nibh euismod tincid laoreet dolore magna aliquam erat volutpat. Ut wisi enim ad minim veniam, quis nostrud extation ullamcorper suscipit lobortis nisl ut aliquip commodo consequat. Duis autem veum iriure dolor in hendrerit in vulputate velit esse molestie consequat.</p>
  <div class="name">Customer Name</div>
  <div class="rate"><span style="color:#f97b1c">★★★★</span><span style="color:#bbb">★</span><em>30 Review</em></div>
</article>
<article class="review" style="left:788px">
  <div class="q">&ldquo;</div>
  <h3>Consectetuer Adipiscing Elit</h3>
  <div class="sub">Sed Diam Nonummy Nibh Euismod...</div>
  <p>Lorem ipsum dolor sit amet, consectetuer adipiscing elit, sed diam nonummy nibh euismod tincid laoreet dolore magna aliquam erat volutpat. Ut wisi enim ad minim veniam, quis nostrud extation ullamcorper suscipit lobortis nisl ut aliquip commodo consequat. Duis autem veum iriure dolor in hendrerit in vulputate velit esse molestie consequat.</p>
  <div class="name">Customer Name</div>
  <div class="rate"><span style="color:#f97b1c">★★★★</span><span style="color:#bbb">★</span><em>30 Review</em></div>
</article>

<section class="newsletter">
  <svg class="abs" style="left:38px;top:6px" width="110" height="100" viewBox="0 0 110 100"><path d="M4 40L104 4 78 94 52 62z M52 62L104 4" fill="none" stroke="rgba(255,255,255,.18)" stroke-width="6"/></svg>
  <h2>SIGNUP FOR NEWSLETTER</h2>
  <small>Incarcatoare Universale Incarcatoare</small>
  <div class="mail">Enter Your Mail ID</div>
  <div class="sub-btn">SUBSCRIBE</div>
  <span class="social" style="left:867px">VLNA</span>
  <span class="social" style="left:925px">KLIK</span>
  <span class="social" style="left:985px">ZÓNA</span>
  <span class="social" style="left:1043px">FOTO</span>
</section>

<footer class="site-footer">
  <div class="contact" style="left:273px">
    <span class="dot"><svg width="14" height="16" viewBox="0 0 14 16"><path d="M7 0a6 6 0 0 1 6 6c0 4-6 10-6 10S1 10 1 6a6 6 0 0 1 6-6z" fill="#fff"/><circle cx="7" cy="6" r="2.2" fill="#f97b1c"/></svg></span>
    <span style="font-size:11px;line-height:15px;width:220px;white-space:nowrap">Built by award, builder, uilt by award<br>No.: 215</span>
  </div>
  <div class="contact" style="left:548px">
    <span class="dot"><svg width="14" height="14" viewBox="0 0 14 14"><path d="M3 1l3 3-2 2a8 8 0 0 0 4 4l2-2 3 3-2 2C6 13 1 8 1 3z" fill="#fff"/></svg></span>
    <span style="font-size:16px">0123 456 789</span>
  </div>
  <div class="contact" style="left:742px">
    <span class="dot"><svg width="14" height="10" viewBox="0 0 14 10"><rect x="1" y="1" width="12" height="8" fill="none" stroke="#fff" stroke-width="1.5"/><path d="M1 1l6 5 6-5" fill="none" stroke="#fff" stroke-width="1.5"/></svg></span>
    <span style="font-size:12px">yourname@domain.com</span>
  </div>
  <div class="footer-rule"></div>
  <nav class="footer-nav">
    <a style="left:113px">About Us</a>
    <a style="left:209px">Faq</a>
    <a style="left:272px">Contact</a>
  </nav>
  <div class="copy">© All Rights Reserved 2017.</div>
</footer>

</body>
</html>
```